Construction Company Stationary Design

We have previously utilised MakerHive to develop a new logo, we wanted to implement it for a while to ensure we liked it before rolling out new stationary. The time has come and we require:
Business Cards
"With Compliments" Cards
Asset Stickers
Vehicle Stickers
Letterhead
Document Header
Invoice Header
Cover Page
We are an established Construction Company working in Northern Australia (outback) that is venturing into a more corporate environment. We DO NOT do residential construction, we focus on commercial & government (Defence, schools, health etc) and work in both urban and remote environments.
Business Card Requirements:
• Logo
• Company Name
• Staff Name
• Staff Position
• Company Physical & Postal Address
• ABN
• Staff Mobile
• Staff Direct Phone (if applicable)
• Staff Email
• Office Phone
• Office Fax
"With Compliments" cards to be much the same as the business cards but with company details only (no staff details)
Asset stickers again to be much the same but with a space to write in asset number.
Document header requires 4 spaces to enter details much like our previous one attached.
We appreciate that designers time is valuable and would request that samples only be produced for one or two of the required items (say Business Card & Letterhead) and await a feedback score of 4 or more prior to producing the full suite of stationary.
If you require any further information please do not hesitate to contact me. lionel@brevmark.com.au

```html
<!DOCTYPE html>
<html lang="en">
<head>
<meta charset="utf-8">
<title>Kestrel Ridge Constructions – Business Card</title>
<link href="https://fonts.googleapis.com/css2?family=Jost:wght@400;600&family=Open+Sans:wght@400&display=swap" rel="stylesheet">
<style>
  :root {
    --backdrop: #c1d0cf;
    --shadow: #a1b4b4;
    --paper: #ffffff;
    --charcoal: #16191c;
    --ink: #1f2224;
    --flame: #ff3813;
    --text-light: #ffffff;
    --dash: #5a5e62;
  }
  * { margin: 0; padding: 0; box-sizing: border-box; }
  html, body { width: 1200px; height: 1075px; overflow: hidden; }
  body { background: var(--backdrop); position: relative; font-family: "Open Sans", sans-serif; }

  .card { position: absolute; width: 753px; background: var(--paper); }
  .card-shadow { position: absolute; width: 753px; background: var(--shadow); }

  .card--front { left: 229px; top: 41px; height: 451px; }
  .shadow--front { left: 245px; top: 58px; height: 451px; }
  .card--back { left: 223px; top: 539px; height: 452px; }
  .shadow--back { left: 239px; top: 556px; height: 452px; }

  .brand { position: absolute; left: 66px; top: 78px; display: flex; align-items: center; gap: 14px; }
  .brand-square { width: 30px; height: 30px; background: var(--flame); }
  .brand-name { font-family: "Jost", sans-serif; font-weight: 600; color: var(--ink); line-height: 1.05; letter-spacing: 1px; }
  .brand-name span { display: block; }
  .brand-name .line-1 { font-size: 34px; }
  .brand-name .line-2 { font-size: 17px; letter-spacing: 3px; }

  .accent-rule { position: absolute; left: 0; top: 219px; width: 100%; height: 3px; background: var(--flame); }
  .info-band { position: absolute; left: 0; top: 226px; width: 100%; height: 225px; background: var(--charcoal); }
  .band-dashes { position: absolute; left: 0; top: 0; width: 100%; height: 6px; }

  .staff { position: absolute; left: 56px; top: 70px; font-family: "Jost", sans-serif; }
  .staff-name { color: var(--flame); font-size: 35px; font-weight: 400; line-height: 1; }
  .staff-role { color: var(--text-light); font-size: 17px; margin-top: 8px; }

  .contacts { position: absolute; left: 427px; top: 44px; list-style: none; color: var(--text-light); font-size: 16px; }
  .contacts li { display: flex; align-items: center; height: 38px; }
  .contacts svg { width: 22px; height: 22px; margin-right: 8px; fill: var(--flame); }
  .contacts .address { margin-left: -8px; height: 30px; }

  .back-name { position: absolute; inset: 0; display: flex; flex-direction: column; justify-content: center; align-items: center; font-family: "Jost", sans-serif; font-weight: 600; color: var(--ink); letter-spacing: 2px; }
  .back-name .line-1 { font-size: 78px; line-height: 1; }
  .back-name .line-2 { font-size: 32px; letter-spacing: 8px; margin-top: 10px; }
</style>
</head>
<body>
  <div class="card-shadow shadow--front"></div>
  <section class="card card--front">
    <div class="brand">
      <div class="brand-square"></div>
      <div class="brand-name"><span class="line-1">KESTREL RIDGE</span><span class="line-2">CONSTRUCTIONS</span></div>
    </div>
    <div class="accent-rule"></div>
    <div class="info-band">
      <svg class="band-dashes" viewBox="0 0 753 6" preserveAspectRatio="none">
        <line x1="0" y1="3" x2="753" y2="3" stroke="var(--dash)" stroke-width="4" stroke-dasharray="9 5"/>
      </svg>
      <div class="staff">
        <p class="staff-name">Owen Tarrant</p>
        <p class="staff-role">Genral Manager</p>
      </div>
      <ul class="contacts">
        <li><svg viewBox="0 0 24 24"><path d="M6.6 10.8a15 15 0 0 0 6.6 6.6l2.2-2.2a1 1 0 0 1 1-.25 11 11 0 0 0 3.6.6 1 1 0 0 1 1 1V20a1 1 0 0 1-1 1A17 17 0 0 1 3 4a1 1 0 0 1 1-1h3.5a1 1 0 0 1 1 1c0 1.25.2 2.45.6 3.6a1 1 0 0 1-.25 1z"/></svg>+61 8 8900 4512 , FAX#</li>
        <li><svg viewBox="0 0 24 24"><path d="M2 5h20v14H2z M2 5l10 8 10-8" stroke="var(--charcoal)" stroke-width="1.6"/></svg>info@kestrelridge.com</li>
        <li><svg viewBox="0 0 24 24"><path d="M9 15l6-6M10.5 6.5l1.5-1.5a4 4 0 0 1 6 6l-1.5 1.5M13.5 17.5l-1.5 1.5a4 4 0 0 1-6-6l1.5-1.5" fill="none" stroke="var(--flame)" stroke-width="2.6" stroke-linecap="round"/></svg>www.kestrelridge.com</li>
        <li class="address">123456 Marlow St Darwin, NT 0800</li>
      </ul>
    </div>
  </section>

  <div class="card-shadow shadow--back"></div>
  <section class="card card--back">
    <div class="back-name"><span class="line-1">KESTREL RIDGE</span><span class="line-2">CONSTRUCTIONS</span></div>
  </section>
</body>
</html>
```